Business Card, Stationary Layout, AND Powerpoint template for an IT Services Company
Silver Harbor Systems
Business Card, Stationary Layout, AND Powerpoint template for an IT Services Company - Information Technology
Creative Brief
Modern
Dean Harrow
President & CEO
40627 Birch Hollow Ln. Fernwick, OR 20349
Dean.Harrow@SilverHarborSystems.example
www.silverharborsystems.example
Perhaps a very light version of my logo graphic.

```html
<!DOCTYPE html>
<html lang="en">
<head>
<meta charset="utf-8">
<title>Silver Harbor Systems — Business Card</title>
<link rel="stylesheet" href="https://fonts.googleapis.com/css2?family=Open+Sans:wght@400;600;700&display=swap">
<style>
  :root {
    --page-bg: #e9ebef;
    --brand-blue: #3f5f9e;
    --brand-blue-light: #5f7fbf;
    --brand-blue-dark: #34508a;
    --ink: #4a4f57;
    --ink-soft: #6d737c;
    --accent: #2f86c8;
    --paper: #ffffff;
    --rule: #c9d1df;
  }
  * { box-sizing: border-box; margin: 0; padding: 0; }
  html, body {
    width: 1200px; height: 988px; overflow: hidden;
    background: var(--page-bg);
    font-family: "Open Sans", Arial, sans-serif;
  }
  .sheet {
    width: 1200px; height: 988px;
    display: flex; flex-direction: column; align-items: center; justify-content: center;
    gap: 44px;
  }
  .card {
    width: 760px; height: 434px; position: relative; overflow: hidden;
    box-shadow: 0 6px 18px rgba(30, 40, 60, .18);
  }

  /* Back side */
  .card-back {
    background: radial-gradient(ellipse at 50% 40%, var(--brand-blue-light), var(--brand-blue) 60%, var(--brand-blue-dark));
    color: #fff;
  }
  .back-mark {
    position: absolute; left: 0; right: 0; top: 130px;
    display: flex; flex-direction: column; align-items: center; gap: 18px;
  }
  .mark-dot {
    width: 96px; height: 96px; border-radius: 50%;
    background: rgba(255,255,255,.9);
  }
  .back-name {
    font-size: 22px; font-weight: 700; letter-spacing: 3px; text-transform: uppercase;
  }
  .back-web {
    position: absolute; left: 0; right: 0; bottom: 46px; text-align: center;
    font-size: 22px; font-weight: 600; letter-spacing: 3px;
  }

  /* Front side */
  .card-front { background: var(--paper); color: var(--ink); }
  .front-logo {
    position: absolute; top: 44px; left: 0; right: 0;
    display: flex; justify-content: center; align-items: center; gap: 16px;
  }
  .logo-dot { width: 62px; height: 62px; border-radius: 50%; background: var(--accent); }
  .logo-name {
    font-size: 34px; font-weight: 600; color: var(--ink); letter-spacing: 1px; text-transform: uppercase;
  }
  .address {
    position: absolute; left: 70px; top: 196px; width: 270px;
    font-size: 14px; line-height: 1.5; color: var(--ink-soft); text-align: right;
  }
  .contact {
    position: absolute; left: 396px; top: 168px;
  }
  .person-name { font-size: 17px; font-weight: 700; color: var(--brand-blue); }
  .person-title { font-size: 13px; color: var(--ink-soft); margin-bottom: 12px; }
  .contact-list { list-style: none; }
  .contact-list li {
    display: flex; align-items: center; gap: 9px;
    font-size: 13px; color: var(--ink-soft); line-height: 24px;
  }
  .contact-list svg { width: 16px; height: 16px; flex: none; }
  .rule-thin {
    position: absolute; left: 0; right: 0; height: 2px; background: var(--rule);
  }
  .rule-thin.upper { bottom: 94px; }
  .rule-thin.lower { bottom: 86px; background: var(--brand-blue-light); }
  .front-band {
    position: absolute; left: 0; right: 0; bottom: 26px; height: 52px;
    background: var(--brand-blue);
    display: flex; align-items: center; justify-content: center;
    color: #fff; font-size: 21px; font-weight: 600; letter-spacing: 3px;
  }
</style>
</head>
<body>
<main class="sheet">
  <section class="card card-back" aria-label="Business card back">
    <div class="back-mark">
      <span class="mark-dot"></span>
      <span class="back-name">Silver Harbor Systems</span>
    </div>
    <p class="back-web">www.SilverHarborSystems.example</p>
  </section>

  <section class="card card-front" aria-label="Business card front">
    <div class="front-logo">
      <span class="logo-dot"></span>
      <span class="logo-name">Silver Harbor Systems</span>
    </div>

    <p class="address">40627 Birch Hollow Ln.<br>Fernwick, OR 20349</p>

    <div class="contact">
      <p class="person-name">Dean Harrow</p>
      <p class="person-title">President &amp; CEO</p>
      <ul class="contact-list">
        <li>
          <svg viewBox="0 0 16 16"><circle cx="8" cy="8" r="8" fill="#4a4f57"/><path d="M5.2 4.2l1.5-.3.8 2-1 .8a6 6 0 0 0 2.8 2.8l.8-1 2 .8-.3 1.5c-4 .3-6.9-2.6-6.6-6.6z" fill="#fff"/></svg>
          (555) 014-2276
        </li>
        <li>
          <svg viewBox="0 0 16 16"><circle cx="8" cy="8" r="8" fill="#4a4f57"/><rect x="4" y="5" width="8" height="6" fill="none" stroke="#fff" stroke-width="1.2"/><path d="M4 5l4 3.4L12 5" fill="none" stroke="#fff" stroke-width="1.2"/></svg>
          Dean.Harrow@SilverHarborSystems.example
        </li>
        <li>
          <svg viewBox="0 0 16 16"><circle cx="8" cy="8" r="8" fill="#4a4f57"/><circle cx="8" cy="8" r="4" fill="none" stroke="#fff" stroke-width="1.1"/><path d="M4 8h8M8 4c-2 2.4-2 5.6 0 8M8 4c2 2.4 2 5.6 0 8" fill="none" stroke="#fff" stroke-width="1"/></svg>
          www.silverharborsystems.example
        </li>
      </ul>
    </div>

    <span class="rule-thin upper"></span>
    <span class="rule-thin lower"></span>
    <div class="front-band">www.SilverHarborSystems.example</div>
  </section>
</main>
</body>
</html>
```